Homecare Design. I would like the color to be same as my business cards

Gentle Hearthkeeper & Helper Agency
I would something very light on the eyes.
Easy to read nothing complicated
I want something that demonstrate soft touch

My contact number has change cell: 203-555-0187 office: 2035550142

Target Market(s)

Elderly
people looking for someone to take care of there love ones
Target age starting at 50

Industry/Entity Type

Business

Font styles to use
Serif

Colors
3176b5
3276b5
85acd3
ceddec

Requirements
Must have

Nice to have
• I woluld like something like helping hands
Should not have
• I really don't care to see medical supplies, medication

```html
<!DOCTYPE html>
<html lang="en">
<head>
<meta charset="utf-8">
<title>Gentle Hearthkeeper &amp; Helper Agency – Postcard</title>
<link rel="stylesheet" href="https://fonts.googleapis.com/css2?family=Lato:wght@400;700;900&family=Oswald:wght@500&family=Tinos:wght@700&display=swap">
<style>
  :root{
    --blue:#3176b5;
    --blue-deep:#3276b5;
    --blue-light:#85acd3;
    --blue-pale:#ceddec;
    --ink:#3a3a3a;
    --heading:#3176b5;
    --paper:#ffffff;
    --backdrop:#eceff1;
  }
  *{box-sizing:border-box;margin:0;padding:0}
  html,body{width:900px;height:1200px;overflow:hidden}
  body{background:var(--backdrop);position:relative;font-family:"Lato",Arial,sans-serif;color:var(--ink)}

  .card{position:absolute;left:100px;width:695px;background:var(--paper);overflow:hidden;box-shadow:0 4px 14px rgba(0,0,0,.25)}
  .card--front{top:47px;height:538px;background:linear-gradient(180deg,#fff 60%,#e9e9e9 100%)}
  .card--back{top:615px;height:537px}

  .front-art{position:absolute;inset:0}

  .call-box{position:absolute;left:55px;top:258px;width:220px;height:177px;border-radius:16px;
    background:linear-gradient(135deg,var(--blue-light) 0%,var(--blue) 55%,#245d92 100%);
    border:3px solid #f2f2f2;box-shadow:0 0 0 2px #9a9a9a, 0 3px 6px rgba(0,0,0,.3);
    text-align:center;padding-top:22px}
  .call-box__lead{font-weight:700;font-size:42px;line-height:40px;color:#2b2b2b;letter-spacing:-.5px}
  .call-box__phone{font-family:"Oswald","Arial Narrow",sans-serif;font-weight:500;font-size:31px;color:#fff;margin-top:12px;letter-spacing:.5px}
  .office-line{position:absolute;left:55px;top:440px;width:220px;text-align:center;
    font-weight:700;font-size:15px;color:var(--blue)}

  .name-band{position:absolute;left:0;right:0;top:465px;height:46px;background:var(--blue-light);
    border-top:2px solid var(--blue-pale);border-bottom:2px solid var(--blue-pale);
    display:flex;align-items:center;justify-content:center;
    font-family:"Tinos",Georgia,serif;font-weight:700;font-size:22px;color:#1f1f1f;letter-spacing:.2px;white-space:nowrap}

  .back-art{position:absolute;inset:0}
  .about{position:absolute;left:20px;top:18px;width:400px}
  .section-title{font-weight:700;font-size:24px;color:var(--heading);letter-spacing:.3px}
  .about p{font-size:16px;line-height:20.8px;margin-top:9px;color:#3d3d3d;white-space:nowrap}
  .services{position:absolute;left:18px;top:182px;width:400px}
  .service-list{list-style:none;display:grid;grid-template-columns:186px 200px;margin-top:16px}
  .service-list li{position:relative;padding-left:22px;font-weight:700;font-size:16.5px;line-height:21px;margin-bottom:8px;color:#3a3a3a;white-space:nowrap}
  .service-list li::before{content:"";position:absolute;left:2px;top:6px;width:9px;height:9px;border-radius:50%;background:var(--blue-light);border:1.5px solid var(--blue)}
  .hours{position:absolute;left:45px;top:383px;width:330px;height:88px;border-radius:22px 0 0 22px;
    background:linear-gradient(90deg,var(--blue) 0%,var(--blue-light) 55%,var(--blue-pale) 100%);
    padding:13px 30px 0 0;text-align:right;font-weight:700;font-size:16.5px;line-height:21px;color:#222}
  .hours dt{display:inline;color:#eef4fa}
  .hours dd{display:inline}
  .website{position:absolute;left:18px;top:492px;font-weight:700;font-size:15px;color:#222}
  .stamp-box{position:absolute;left:590px;top:82px;width:75px;height:88px;border:1.5px solid #333}
  .address-line{position:absolute;left:490px;width:175px;height:2px;background:#222}
</style>
</head>
<body>

<section class="card card--front" aria-label="Postcard front">
  <svg class="front-art" width="695" height="538" viewBox="0 0 695 538">
    <defs>
      <linearGradient id="photoTone" x1="0" y1="0" x2="1" y2="1">
        <stop offset="0" stop-color="#d9d5d2"/>
        <stop offset=".45" stop-color="#9c918b"/>
        <stop offset="1" stop-color="#4a403b"/>
      </linearGradient>
    </defs>
    <path role="img" aria-label="Photo of caring hands gently holding an elderly person's hands"
      d="M0,0 H695 V335 C620,395 520,432 430,428 C300,420 160,330 0,300 Z" fill="url(#photoTone)"/>
    <path d="M0,296 C160,326 300,416 430,424 C520,428 620,392 695,330 V352 C620,410 520,440 430,438 C300,434 160,346 0,318 Z" fill="var(--blue)"/>
    <path d="M0,318 C160,346 300,434 430,438 C520,440 620,410 695,352 V362 C620,420 520,448 430,446 C300,442 160,356 0,328 Z" fill="#fff"/>
  </svg>

  <div class="call-box">
    <div class="call-box__lead">CALL US<br>TODAY</div>
    <div class="call-box__phone">203-555-0187</div>
  </div>
  <div class="office-line">Office: 203-555-0142</div>

  <div class="name-band">GENTLE HEARTHKEEPER &amp; HELPER AGENCY</div>
</section>

<section class="card card--back" aria-label="Postcard back">
  <svg class="back-art" width="695" height="537" viewBox="0 0 695 537">
    <defs>
      <linearGradient id="backMist" x1="0" y1="0" x2="1" y2="0">
        <stop offset="0" stop-color="#e2e2e2"/>
        <stop offset=".7" stop-color="#f7f7f7"/>
        <stop offset="1" stop-color="#fff"/>
      </linearGradient>
      <linearGradient id="curveBlue" x1="0" y1="0" x2="0" y2="1">
        <stop offset="0" stop-color="var(--blue)"/>
        <stop offset=".6" stop-color="var(--blue-light)"/>
        <stop offset="1" stop-color="var(--blue-pale)"/>
      </linearGradient>
    </defs>
    <path d="M0,0 H432 C470,70 470,170 440,260 C410,350 395,440 448,537 H0 Z" fill="url(#backMist)"/>
    <path d="M432,0 H452 C488,80 480,190 448,270 C420,350 410,440 470,537 H448 C395,440 410,350 440,260 C470,170 470,70 432,0 Z" fill="url(#curveBlue)"/>
    <path d="M448,537 C420,490 405,450 402,410 C420,460 450,505 500,537 Z" fill="var(--blue-pale)" opacity=".9"/>
  </svg>

  <div class="about">
    <h2 class="section-title">ABOUT&nbsp; US</h2>
    <p>Gentle Hearthkeeper &amp; Helper Agency, assist<br>elderly clients who need assistance in or out of the<br>home. Our home care services to our clients to<br>assist them to lead dignified&nbsp; and independent lives<br>in the comfort and safety of there own homes</p>
  </div>

  <div class="services">
    <h2 class="section-title">OUR SERVICES</h2>
    <ul class="service-list">
      <li>Assistance with<br>daily living</li>
      <li>Run errands</li>
      <li>Companionship</li>
      <li>Doctors visits</li>
      <li>Light Cooking</li>
      <li>light House keeping</li>
      <li>Laundry</li>
      <li>In and out of<br>home activities</li>
    </ul>
  </div>

  <dl class="hours">
    <div><dt>MONDAY - FRIDAY:</dt> <dd>8:00 - 5:00 PM.</dd></div>
    <div><dt>SATURDAY:</dt> <dd>8:00 - 2:00 PM.</dd></div>
    <div><dt>SUNDAY:</dt> <dd>CLOSED</dd></div>
  </dl>

  <div class="website">www.gentlehearthkeeperhelper.com</div>

  <div class="stamp-box" aria-hidden="true"></div>
  <div class="address-line" style="top:287px"></div>
  <div class="address-line" style="top:315px"></div>
  <div class="address-line" style="top:344px"></div>
</section>

</body>
</html>
```